Creat new BusinessCard for Brightpath Advisory!

Hello Creativ Designer. I need a new Businesscard for our brand new Company "Brightpath Coaching". We do Consulting for a better Life & Work Situation. to create Fulfillment, Sense, Motivation and healthy Work Places in Company's. So we try to create a better World and help the employee to like what they do!
So we would like to have 2 Sites on the card. On the Back we want to put this words: "The sole meaning of life, is to serve humanity" (it can be vertical oder horizontal). In the front there is the Logo (Black or White) and Adress+ and Slogan.

Slogan on the front: -Make your Business & Life to a better place-

Name: Lukas Fenwald
Titel: Founder - Visionary - Trainer
Adress: Based in Switzerland

Tel: +41 (0) 71 483 27 15
Email: hello@brightpath-coaching.ch
Homepage: www.brightpath-coaching.ch

Thanks for your inspired Ideas and your help to make the world to a better place! IT has to be ready to print and normal Size.

Target Market(s)

insurance, Bank, Telecom, industry, IT, Medical

Contact Information for Business Card

Breite: 85 mm x Höhe: 55 mm

Colors

Designer to choose colors to be used in the design.

Requirements
Nice to have
• Thanks for your Ideas so far!
• Maybe you can try/play with the colors: Purple Code #652C8F and Grey #979797 from the Zorvik Logo purple and grey (but only a soft combination, not to much)

```html
<!DOCTYPE html>
<html lang="en">
<head>
<meta charset="utf-8">
<title>Brightpath Coaching – Business Card</title>
<link href="https://fonts.googleapis.com/css2?family=Roboto+Condensed:ital,wght@0,400;0,700;1,500&family=Roboto:wght@400&display=swap" rel="stylesheet">
<style>
  :root {
    --stage: #1c1c1c;
    --paper: #f4f4f4;
    --ink: #111111;
    --ink-soft: #3a3a3a;
    --muted: #7a7a7a;
    --rule: #c8c8c8;
    --black: #000000;
    --white: #ffffff;
  }
  html, body {
    margin: 0;
    width: 1200px;
    height: 960px;
    overflow: hidden;
    background: var(--stage);
  }
  .canvas { position: relative; width: 1200px; height: 960px; }

  .card-front {
    position: absolute; left: 314px; top: 113px;
    width: 600px; height: 342px;
    background: var(--paper);
    box-shadow: 0 6px 14px rgba(0,0,0,.6);
  }
  .brand {
    position: absolute; left: 60px; top: 106px; width: 198px;
    display: flex; flex-direction: column; align-items: center;
  }
  .brand-mark { width: 82px; height: 82px; border-radius: 50%; background: var(--ink); }
  .brand-name {
    margin-top: 14px; text-align: center; line-height: 1.05;
    font: 700 22px "Roboto Condensed", sans-serif;
    color: var(--ink); text-transform: uppercase; letter-spacing: .5px;
  }
  .divider {
    position: absolute; left: 267px; top: 109px;
    width: 1px; height: 133px; background: var(--rule);
  }
  .person { position: absolute; left: 293px; top: 113px; }
  .person-name {
    margin: 0; font: 700 23px "Roboto Condensed", sans-serif;
    color: var(--ink); text-transform: uppercase; line-height: 1;
  }
  .person-title {
    margin: 6px 0 0; font: 400 15px "Roboto Condensed", sans-serif;
    color: var(--muted); text-transform: uppercase; line-height: 1;
  }
  .contacts { list-style: none; margin: 18px 0 0; padding: 0; }
  .contacts li {
    display: flex; align-items: center; gap: 8px;
    font: 400 15px "Roboto", sans-serif; color: var(--ink-soft);
    line-height: 19px;
  }
  .contacts svg { width: 13px; height: 13px; flex: none; fill: var(--ink); }
  .slogan-band {
    position: absolute; left: 0; bottom: 0; width: 100%; height: 34px;
    background: var(--black); border-top: 2px solid #d0d0d0; box-sizing: border-box;
    display: flex; align-items: center; justify-content: center;
    font: italic 500 15px "Roboto Condensed", sans-serif; color: var(--white);
  }

  .card-back {
    position: absolute; left: 312px; top: 472px;
    width: 598px; height: 342px;
    background: var(--black);
    box-shadow: 0 6px 14px rgba(0,0,0,.6);
  }
  .card-back .brand { left: 200px; top: 93px; }
  .card-back .brand-mark { width: 100px; height: 100px; background: var(--white); }
  .card-back .brand-name { color: var(--white); font-size: 26px; }
  .quote {
    position: absolute; left: 0; top: 296px; width: 100%;
    text-align: center; margin: 0;
    font: italic 500 15px "Roboto Condensed", sans-serif; color: var(--white);
  }
</style>
</head>
<body>
<main class="canvas">
  <section class="card-front">
    <div class="brand">
      <div class="brand-mark"></div>
      <div class="brand-name">Brightpath Coaching</div>
    </div>
    <div class="divider"></div>
    <div class="person">
      <h1 class="person-name">Lukas Fenwald</h1>
      <p class="person-title">Founder - Visionary - Trainer</p>
      <ul class="contacts">
        <li>
          <svg viewBox="0 0 24 24" aria-hidden="true"><path d="M6.6 10.8a15.1 15.1 0 0 0 6.6 6.6l2.2-2.2c.3-.3.7-.4 1-.2 1.1.4 2.3.6 3.6.6.6 0 1 .4 1 1V20c0 .6-.4 1-1 1A17 17 0 0 1 3 4c0-.6.4-1 1-1h3.5c.6 0 1 .4 1 1 0 1.3.2 2.5.6 3.6.1.3 0 .7-.2 1z"/></svg>
          +41 (0) 71 483 27 15
        </li>
        <li>
          <svg viewBox="0 0 24 24" aria-hidden="true"><path d="M2 5h20v14H2z" fill="none"/><path d="M2 6v12h20V6l-10 7z"/><path d="M2 5h20l-10 7z"/></svg>
          hello@brightpath-coaching.ch
        </li>
        <li>
          <svg viewBox="0 0 24 24" aria-hidden="true"><circle cx="12" cy="12" r="10"/><path d="M7 7c2 1 2 3 4 3s1 3 3 3l-1 4c2 0 4-3 4-5s-2-2-2-4 1-3 1-3" fill="#f4f4f4"/></svg>
          www.brightpath-coaching.ch
        </li>
      </ul>
    </div>
    <div class="slogan-band">Make your Business &amp; Life to a better place</div>
  </section>

  <section class="card-back">
    <div class="brand">
      <div class="brand-mark"></div>
      <div class="brand-name">Brightpath Coaching</div>
    </div>
    <p class="quote">The sole meaning of life, is to serve humanity</p>
  </section>
</main>
</body>
</html>
```